Income Tax Business Cards - Updates

Need to update these business cards while keeping all the same wording but just update them and make them look nicer and more modern/ on brand with our brand.

Industry/Entity Type

finance

Contact Information for Business Card

we have multiple locations so will just need to easily be able to change the address and phone numbers

Colors

Designer to choose colors to be used in the design.

```html
<!DOCTYPE html>
<html lang="en">
<head>
<meta charset="utf-8">
<title>Ledgerline Financial Group – Business Card</title>
<link rel="stylesheet" href="https://fonts.googleapis.com/css2?family=Roboto:wght@400;500;700&family=Fira+Sans:wght@700;800&display=swap">
<style>
  :root {
    --backdrop: #9a9b9a;
    --paper: #fbfbfb;
    --green: #11502f;
    --red: #c8202a;
    --ink: #3a3a3a;
    --white: #ffffff;
  }
  * { box-sizing: border-box; margin: 0; padding: 0; }
  html, body { width: 1200px; height: 1200px; overflow: hidden; }
  body { background: var(--backdrop); position: relative; font-family: "Roboto", sans-serif; }

  .card { position: absolute; left: 231px; width: 737px; height: 450px; overflow: hidden; }
  .card-front { top: 116px; background: var(--paper); border-radius: 0 36px 0 36px; }
  .card-back  { top: 632px; background: var(--green); border-radius: 36px 0 36px 0; }

  .front-wave { position: absolute; left: 0; bottom: 0; width: 737px; height: 100px; }

  .brand { position: absolute; font-family: "Roboto", sans-serif; font-weight: 500; text-align: center; line-height: 1.05; }
  .brand-front { left: 47px; top: 180px; width: 296px; color: var(--green); font-size: 40px; }
  .brand-back  { left: 446px; top: 320px; width: 256px; color: var(--white); font-size: 34px; }
  .brand small { display: block; font-size: 0.38em; letter-spacing: 0.3em; margin-top: 8px; }

  .divider { position: absolute; left: 369px; top: 142px; width: 2px; height: 168px; background: var(--red); }

  .person { position: absolute; left: 402px; top: 140px; }
  .person-name { color: var(--green); font-weight: 700; font-size: 28px; letter-spacing: 0.01em; }
  .person-title { color: var(--red); font-weight: 400; font-size: 22px; margin-top: 2px; }

  .contacts { position: absolute; left: 402px; top: 220px; list-style: none; }
  .contacts li { display: flex; align-items: center; height: 33px; font-size: 20px; color: var(--ink); }
  .contacts svg { width: 20px; height: 20px; margin-right: 11px; flex: none; }

  .headline { position: absolute; left: 40px; width: 360px; text-align: center; font-family: "Fira Sans", sans-serif; font-weight: 800; line-height: 1; }
  .headline-top { top: 170px; color: var(--white); font-size: 50px; }
  .headline-main { top: 226px; color: var(--red); font-size: 54px; letter-spacing: -0.02em;
    text-shadow: 3px 0 0 #fff, -3px 0 0 #fff, 0 3px 0 #fff, 0 -3px 0 #fff, 2px 2px 0 #fff, -2px -2px 0 #fff, 2px -2px 0 #fff, -2px 2px 0 #fff; }

  .offer-band { position: absolute; left: 0; top: 330px; width: 737px; height: 90px; }
  .offer { position: absolute; left: 40px; width: 385px; text-align: center; font-family: "Fira Sans", sans-serif; font-weight: 800; color: var(--white); line-height: 1; letter-spacing: -0.02em;
    text-shadow: 3px 0 0 var(--red), -3px 0 0 var(--red), 0 3px 0 var(--red), 0 -3px 0 var(--red), 2px 2px 0 var(--red), -2px -2px 0 var(--red), 2px -2px 0 var(--red), -2px 2px 0 var(--red); }
  .offer-amount { top: 336px; font-size: 50px; }
  .offer-note { top: 385px; font-size: 32px; }
</style>
</head>
<body>

<section class="card card-front" aria-label="Card front">
  <div class="brand brand-front">Ledgerline<small>FINANCIAL GROUP</small></div>
  <div class="divider"></div>

  <div class="person">
    <p class="person-name">MARCUS ELDEN</p>
    <p class="person-title">President</p>
  </div>

  <ul class="contacts">
    <li><svg viewBox="0 0 20 20"><path fill="#c8202a" d="M2 7c2-3 14-3 16 0l-1 2-4-1V6H7v2L3 9zM5 10h10l2 6H3z"/><circle cx="10" cy="13" r="2" fill="#fff"/></svg>012 3456 7890</li>
    <li><svg viewBox="0 0 20 20"><rect x="1" y="4" width="15" height="11" fill="#c8202a"/><path d="M1 4l7.5 6L16 4" fill="none" stroke="#fff" stroke-width="1.5"/><circle cx="16" cy="15" r="4" fill="#c8202a" stroke="#fff"/><path d="M14 15l1.5 1.5 2.5-3" fill="none" stroke="#fff" stroke-width="1.3"/></svg>info@yourmail.com</li>
    <li><svg viewBox="0 0 20 20" fill="none" stroke="#c8202a" stroke-width="1.5"><circle cx="10" cy="10" r="8"/><ellipse cx="10" cy="10" rx="3.5" ry="8"/><path d="M2 10h16M3.5 6h13M3.5 14h13"/></svg>www.yourwebside.com</li>
  </ul>

  <svg class="front-wave" viewBox="0 0 737 100" preserveAspectRatio="none" aria-hidden="true">
    <path d="M0 100V34C180 68 500 72 737 0V100Z" fill="var(--green)"/>
    <path d="M0 22C170 58 420 66 562 48C420 62 170 56 0 38Z" fill="var(--red)"/>
    <path d="M0 38C170 56 420 62 562 48C440 68 200 72 0 44Z" fill="var(--paper)"/>
  </svg>
</section>

<section class="card card-back" aria-label="Card back">
  <p class="headline headline-top">FILE YOUR</p>
  <p class="headline headline-main">TAXES HERE</p>

  <svg class="offer-band" viewBox="0 0 737 90" aria-hidden="true" style="top:280px;height:140px">
    <path d="M33 17C150 10 300 8 410 12" fill="none" stroke="var(--white)" stroke-width="5" stroke-linecap="round"/>
    <rect x="0" y="63" width="432" height="64" fill="var(--red)"/>
    <rect x="709" y="63" width="28" height="64" fill="var(--red)"/>
    <path d="M0 69h18v-18l27 44-27 44v-18H0" fill="none" stroke="var(--white)" stroke-width="3"/>
    <path d="M432 69h-18v-18l-27 44 27 44v-18h18" fill="none" stroke="var(--white)" stroke-width="3"/>
    <path d="M709 69h-18M709 121h-18" stroke="var(--white)" stroke-width="3"/>
  </svg>

  <p class="offer offer-amount">UP TO $6,000</p>
  <p class="offer offer-note">SAME DAY ADVANCE</p>

  <div class="brand brand-back">Ledgerline<small>FINANCIAL GROUP</small></div>
</section>

</body>
</html>
```